Brightwater Spectral Inquiry Website

We are a paranormal research group located in Central Mississippi. We are a group dedicated to help the community in any paranormal investigation. We use fresh new techniques with cutting edge technology to investigate any paranormal situation. Our services are always free of charge to anyone. An unique feature of our group is that we provide a complete history of the property, courtesy of our research team. We would like to see designs that incorporate our logo. We are a professional group and want a professional website.. we will need a home page that will reflect out goals. Links will include "Home, About Us, Contact us, (MAYBE MORE). We will also want a "blank page" with same links that we can edit and fill in all the information..

Target Market(s)

Paranormal-Ghost hunting groups

Industry/Entity Type

Community

Coding

Coded - Design and coding required

Number of Pages Required

2 page

Font styles to use
Other font styles liked:

Requirements
Must have
• we will need a home page that will reflect out goals. Links will include "Home, About Us, Contact us, (MAYBE MORE). We will also want a "blank page" with same links that we can edit and fill in all the information..

```html
<!DOCTYPE html>
<html lang="en">
<head>
<meta charset="utf-8">
<title>Brightwater Spectral Inquiry</title>
<link rel="stylesheet" href="https://fonts.googleapis.com/css2?family=Open+Sans:ital,wght@0,400;0,600;1,400&family=Oswald:wght@400;600&display=swap">
<style>
:root{
  --sky-top:#8fdbe6;
  --sky-mid:#c9eef3;
  --page:#ffffff;
  --red:#b30000;
  --nav-red:#a80a0a;
  --ink:#1c1c1c;
  --body:#555555;
  --muted:#8a8a8a;
  --blue:#1d6c98;
  --strip:#0c1a24;
  --cyan:#35b8e8;
  --footer:#141414;
}
*{box-sizing:border-box;margin:0;padding:0}
html,body{width:1199px;height:1200px;overflow:hidden}
body{position:relative;font-family:"Open Sans",Arial,sans-serif;background:var(--page)}
.backdrop{position:absolute;left:0;top:0;width:1199px;height:1126px;
  background:linear-gradient(180deg,var(--sky-top) 0%,var(--sky-mid) 45%,#eef9fb 75%,#ffffff 100%)}
.page{position:absolute;left:104px;top:525px;width:992px;height:601px;background:var(--page)}
.social{position:absolute;top:14px;left:992px;display:flex;gap:6px}
.social span{width:26px;height:26px;border-radius:50%;background:#111}
.nav{position:absolute;top:60px;left:715px;display:flex;gap:3px}
.nav a{display:block;height:46px;line-height:46px;background:var(--nav-red);color:#fff;text-decoration:none;
  font-size:15px;letter-spacing:1.5px;text-align:center}
.nav .home{width:89px}.nav .about{width:130px}.nav .contact{width:155px}
.hero{position:absolute;left:104px;top:107px;width:992px;height:418px;
  background:radial-gradient(ellipse at 60% 35%,#b9c6d6 0%,#5d7190 25%,#1d2c4a 60%,#0b1226 100%)}
.brand{position:absolute;left:130px;top:40px;display:flex;align-items:center;gap:12px;
  color:#fff;font-size:22px;font-weight:600}
.brand i{width:22px;height:22px;background:#fff;border-radius:50%}
.hero-title{position:absolute;right:20px;bottom:20px;color:#fff;font-family:"Oswald",Arial,sans-serif;
  font-weight:600;font-size:33px;letter-spacing:-.3px;text-transform:uppercase}
.intro-title{position:absolute;left:129px;top:560px;font-size:36px;line-height:36px;color:var(--ink);
  text-transform:uppercase;font-weight:400}
.intro-title b{color:var(--red);font-weight:400}
.intro-text{position:absolute;left:130px;top:679px;width:405px;font-size:14px;line-height:16.5px;color:var(--body)}
.know-more{position:absolute;left:133px;top:786px;font-family:"Oswald",Arial,sans-serif;font-size:17px;color:#333;text-decoration:none}
.know-more span{color:var(--blue);font-size:13px;margin-left:6px}
.agent-photo{position:absolute;left:560px;top:598px;width:208px;height:209px;
  background:radial-gradient(circle at 58% 62%,#ffffff 0%,#b5b5b5 12%,#333 45%,#0a0a0a 80%)}
.questions{position:absolute;left:784px;top:598px;width:266px;height:209px;background:var(--blue);color:#fff;padding:14px 15px}
.questions h2{font-family:"Oswald",Arial,sans-serif;font-size:21px;font-weight:600;margin-bottom:14px}
.questions p{font-size:13px;line-height:15px}
.questions .lbl{color:#111}
.questions em{font-style:italic}
.more-strip{position:absolute;left:1050px;top:598px;width:44px;height:209px;background:var(--strip)}
.more-strip span{position:absolute;left:50%;top:50%;transform:translate(-50%,-50%) rotate(-90deg);
  white-space:nowrap;font-family:"Oswald",Arial,sans-serif;font-size:24px;color:var(--cyan)}
.feature{position:absolute;top:852px;width:280px;text-align:center}
.feature svg{display:block;margin:0 auto}
.feature h3{font-size:22px;font-weight:400;color:var(--red);margin-top:8px;text-transform:uppercase}
.feature p{font-size:14px;line-height:16.5px;color:var(--muted);margin-top:14px}
.footer{position:absolute;left:0;top:1126px;width:1199px;height:74px;
  background:linear-gradient(180deg,#3a3a3a 0%,var(--footer) 30%,#1f1f1f 100%);color:#d6d6d6;font-size:12.5px;line-height:21px;padding:14px 110px}
</style>
</head>
<body>
<div class="backdrop" role="img" aria-label="Misty cyan forest with bare trees"></div>

<div class="social" aria-label="Social links"><span></span><span></span><span></span></div>

<nav class="nav">
  <a class="home" href="#">HOME</a>
  <a class="about" href="#">ABOUT US</a>
  <a class="contact" href="#">CONTACT US</a>
</nav>

<div class="hero" role="img" aria-label="Outstretched hand reaching through swirling smoke">
</div>
<div class="brand"><i></i>Brightwater Spectral Inquiry</div>
<div class="hero-title" style="position:absolute;left:auto;right:123px;top:458px;bottom:auto">Brightwater Spectral Investigation &amp; Research</div>

<main class="page"></main>

<h1 class="intro-title"><b>B</b>rightwater<br><b>S</b>pectral<br><b>I</b>nquiry</h1>
<p class="intro-text">Praesent vestibulum aenean nonummy hendrerit mauris. Cum sociis natoque penatibus et magnis dis parturient montes ascetur ridiculus mus. Nulla dui. Fusce feugiat malesuada odio. Morbi nunc odio gravida at cursus nec luctus a lorem. Maece-nas tristique orci ac sem. Duis ultricies pharetra magna.</p>
<a class="know-more" href="#">know more<span>»</span></a>

<div class="agent-photo" role="img" aria-label="Investigator in a dark suit holding a flashlight"></div>
<section class="questions">
  <h2>QUESTIONS?</h2>
  <p><span class="lbl">Call:</span> 01555-320-47-16<br><span class="lbl">Email:</span> info@brightwaterinquiry.org</p>
  <p style="margin-top:14px">Agents available for assistance -<br><em>7AM - 9PM PT</em></p>
  <p style="margin-top:14px"><em>After hour inquiries will be addressed within 24 hours.</em></p>
</section>
<div class="more-strip"><span>More Information...</span></div>

<section class="feature" style="left:126px">
  <svg width="94" height="100" viewBox="0 0 94 100" aria-hidden="true">
    <g fill="none" stroke="#222" stroke-width="3">
      <ellipse cx="47" cy="50" rx="44" ry="16"/>
      <ellipse cx="47" cy="50" rx="44" ry="16" transform="rotate(60 47 50)"/>
      <ellipse cx="47" cy="50" rx="44" ry="16" transform="rotate(-60 47 50)"/>
    </g>
    <circle cx="47" cy="50" r="14" fill="#fff" stroke="#222" stroke-width="2"/>
    <text x="47" y="57" text-anchor="middle" font-family="Oswald,sans-serif" font-size="19" font-weight="600" fill="#222">1</text>
  </svg>
  <h3>Investigations</h3>
  <p>A visit from a family members causes unrest but more is at hand then just a visit from Grandpa. The team works to put all the pieces together to explain all the activity.</p>
</section>

<section class="feature" style="left:461px">
  <svg width="94" height="100" viewBox="0 0 94 100" aria-hidden="true">
    <g fill="none" stroke="#222" stroke-width="3">
      <ellipse cx="47" cy="50" rx="44" ry="16"/>
      <ellipse cx="47" cy="50" rx="44" ry="16" transform="rotate(60 47 50)"/>
      <ellipse cx="47" cy="50" rx="44" ry="16" transform="rotate(-60 47 50)"/>
    </g>
    <circle cx="47" cy="50" r="14" fill="#fff" stroke="#222" stroke-width="2"/>
    <text x="47" y="57" text-anchor="middle" font-family="Oswald,sans-serif" font-size="19" font-weight="600" fill="#222">2</text>
  </svg>
  <h3>Ghost Hunting</h3>
  <p>What is ghost hunting?<br>some of the do's and don'ts. Find out more about what we do and our opinion on Ghost hunting. What does it take to find the proof to satisfy the skeptics?</p>
</section>

<section class="feature" style="left:782px">
  <svg width="94" height="100" viewBox="0 0 94 100" aria-hidden="true">
    <g fill="none" stroke="#222" stroke-width="3">
      <ellipse cx="47" cy="50" rx="44" ry="16"/>
      <ellipse cx="47" cy="50" rx="44" ry="16" transform="rotate(60 47 50)"/>
      <ellipse cx="47" cy="50" rx="44" ry="16" transform="rotate(-60 47 50)"/>
    </g>
    <circle cx="47" cy="50" r="14" fill="#fff" stroke="#222" stroke-width="2"/>
    <text x="47" y="57" text-anchor="middle" font-family="Oswald,sans-serif" font-size="19" font-weight="600" fill="#222">3</text>
  </svg>
  <h3>Latest News</h3>
  <p>Praesent vestibulum aenean nonummy hendrerit mauris. Cum sociis natoque penatibus et magnis dis parturient montes ascetur ridiculus mus. Nulla dui.</p>
</section>

<footer class="footer">
  BRIGHTWATER SPECTRAL INQUIRY<br>
  Copyright © 2014 &nbsp;| All Rights Reserved
</footer>
</body>
</html>
```